Postcard needed for expert witness service

Looking for a professional postcard that will be mailed to personal injury lawyers / law firms to introduce my expert witness services.

Target Market(s)

Law firms, personal injury lawyers

Industry/Entity Type

Expert witness, law

Font styles to use
Sans Serif

Requirements
Must have
• Logo: The Frost Sage [Main Heading]Do you handle snow and ice related slip and falls? Delbert is one of the top snow industry experts in the country! [Following should be in a list type fashion, possibly bulleted]Delbert's credentials: Accredited Winter Technician (AWT), past PRDG board member and chair, former ISO 9001 certified snow company owner , 32 years in the industry. (555) 014-2387 NOTES: Postcard will be 4" x 6" Please use both sides however must have room for labels and stamp
Should not have
• Wouldn't suggest using both photos on same side. Honestly, feel free to only use one of the slip and fall photos if it works out better. Thanks!

```html
<!DOCTYPE html>
<html lang="en">
<head>
<meta charset="utf-8">
<title>The Frost Sage – Postcard</title>
<link href="https://fonts.googleapis.com/css2?family=Oswald:wght@500;600&family=Montserrat:wght@400;500;600&display=swap" rel="stylesheet">
<style>
  :root {
    --stage: #1b1b1b;
    --paper: #ffffff;
    --ink: #111111;
    --tan: #b89f74;
    --navy: #1e2537;
    --rule: #c9c9c9;
    --photo-warm-a: #8e96a3;
    --photo-warm-b: #3e4a63;
    --photo-grey-a: #5a5d63;
    --photo-grey-b: #2a2c30;
  }
  * { margin: 0; padding: 0; box-sizing: border-box; }
  html, body { width: 851px; height: 1200px; overflow: hidden; background: var(--stage); }
  body { position: relative; font-family: "Montserrat", sans-serif; }

  .card { position: absolute; left: 51px; width: 749px; height: 529px; background: var(--paper); overflow: hidden; }
  .card--front { top: 46px; }
  .card--back { top: 608px; }

  .brand { position: absolute; left: 26px; top: 34px; display: flex; align-items: center; gap: 7px; }
  .brand__mark { width: 10px; height: 10px; background: var(--tan); }
  .brand__name { font-family: "Montserrat", sans-serif; font-weight: 600; font-size: 14px; line-height: 1; letter-spacing: 0.3px; color: var(--ink); white-space: nowrap; }
  .card--back .brand { left: 28px; top: 34px; }

  .headline { position: absolute; left: 26px; top: 96px; font-family: "Oswald", sans-serif; font-weight: 600; font-size: 45px; line-height: 42px; color: var(--ink); text-transform: uppercase; letter-spacing: -0.5px; transform: scaleX(0.85); transform-origin: left top; }
  .headline__lead { color: var(--tan); }
  .tagline { position: absolute; left: 26px; top: 264px; font-size: 8.3px; font-weight: 500; color: var(--ink); }

  .credentials { position: absolute; left: 0; top: 305px; width: 315px; height: 79px; }
  .credentials__band { position: absolute; inset: 0; }
  .credentials__title { position: absolute; left: 26px; top: 12px; font-family: "Oswald", sans-serif; font-weight: 500; font-size: 17px; color: var(--paper); transform: scaleX(0.85); transform-origin: left top; white-space: nowrap; }
  .credentials__list { position: absolute; left: 26px; top: 36px; list-style: none; font-size: 7px; line-height: 8px; color: var(--paper); }
  .credentials__list li { position: relative; padding-left: 13px; }
  .credentials__list li::before { content: "•"; position: absolute; left: 0; font-size: 5px; }
  .credentials__seal { position: absolute; left: 224px; top: 15px; width: 48px; height: 48px; border-radius: 50%; border: 2px solid var(--paper); }

  .footer-band { position: absolute; left: 0; right: 0; top: 425px; height: 104px; }
  .footer-band--navy { background: var(--navy); }
  .footer-band--tan { background: var(--tan); }

  .call { position: absolute; font-family: "Oswald", sans-serif; text-transform: uppercase; }
  .call__label { display: block; font-weight: 500; color: var(--paper); transform: scaleX(0.85); white-space: nowrap; }
  .call__phone { display: block; font-weight: 500; white-space: nowrap; transform: scaleX(0.85); }
  .card--front .call { left: 33px; top: 443px; }
  .card--front .call__label { font-size: 25px; line-height: 30px; transform-origin: left top; }
  .card--front .call__phone { font-size: 41px; line-height: 44px; color: var(--tan); transform-origin: left top; }

  .contact { position: absolute; right: 22px; top: 480px; text-align: right; color: var(--paper); font-size: 12.5px; line-height: 17px; font-weight: 500; }

  .photo { position: absolute; box-shadow: 0 6px 14px rgba(0,0,0,0.35); }
  .photo--fall { left: 351px; top: 27px; width: 377px; height: 426px; background: linear-gradient(160deg, #d9dbdf 0%, var(--photo-warm-a) 40%, var(--photo-warm-b) 75%, #5b5e63 100%); }
  .photo--injured { left: 24px; top: 85px; width: 339px; height: 421px; background: linear-gradient(170deg, var(--photo-grey-a) 0%, #3b3d42 45%, var(--photo-grey-b) 100%); }

  .protect { position: absolute; left: 46px; top: 180px; font-family: "Oswald", sans-serif; font-weight: 600; font-size: 63px; line-height: 59px; color: var(--paper); text-transform: uppercase; transform: scaleX(0.85); transform-origin: left top; white-space: nowrap; }
  .protect__accent { color: var(--tan); }

  .stamp-box { position: absolute; left: 592px; top: 51px; width: 135px; height: 135px; border: 1.5px solid var(--rule); }
  .address-line { position: absolute; left: 501px; width: 229px; height: 1.5px; background: var(--rule); }

  .card--back .call { right: 22px; top: 441px; text-align: right; }
  .card--back .call__label { font-size: 22px; line-height: 26px; transform-origin: right top; }
  .card--back .call__phone { font-size: 34px; line-height: 36px; color: var(--paper); transform-origin: right top; }
  .card--back .call__address { display: block; font-weight: 500; font-size: 14.5px; line-height: 18px; color: var(--paper); transform: scaleX(0.82); transform-origin: right top; white-space: nowrap; }
</style>
</head>
<body>

<section class="card card--front">
  <div class="brand">
    <span class="brand__mark"></span>
    <span class="brand__name">THE FROST SAGE</span>
  </div>

  <h1 class="headline">
    <span class="headline__lead">Do you handle</span><br>
    Snow &amp; Ice<br>
    Related<br>
    Slip and Falls?
  </h1>
  <p class="tagline">Delbert is one of the top snow industry experts in the country!</p>

  <div class="credentials">
    <svg class="credentials__band" viewBox="0 0 315 79" width="315" height="79" aria-hidden="true">
      <polygon points="0,0 277,0 315,79 0,79" fill="var(--tan)"/>
    </svg>
    <h2 class="credentials__title">DELBERT'S CREDENTIALS</h2>
    <ul class="credentials__list">
      <li>Accredited Winter Technician (AWT)</li>
      <li>Past PRDG board member and chair</li>
      <li>Former ISO 9001 certified snow company owner</li>
      <li>32 years in the industry.</li>
    </ul>
    <div class="credentials__seal"></div>
  </div>

  <div class="footer-band footer-band--navy"></div>
  <div class="photo photo--fall" role="img" aria-label="Photo of a person slipping and falling on an icy city sidewalk"></div>

  <div class="call">
    <span class="call__label">Call now today!</span>
    <span class="call__phone">(555) 014-2387</span>
  </div>
  <div class="contact">
    <p>www.askthefrostsage.com</p>
    <p>delbert@askthefrostsage.com</p>
  </div>
</section>

<section class="card card--back">
  <div class="brand">
    <span class="brand__mark"></span>
    <span class="brand__name">THE FROST SAGE</span>
  </div>

  <div class="footer-band footer-band--tan"></div>
  <div class="photo photo--injured" role="img" aria-label="Black and white photo of a woman in a winter coat and knit hat hurt after a fall on ice"></div>
  <h2 class="protect">
    Protecting<br>
    Yourself<br>
    &amp; <span class="protect__accent">Seeking</span><br>
    <span class="protect__accent">Justice</span>
  </h2>

  <div class="stamp-box"></div>
  <div class="address-line" style="top:255px"></div>
  <div class="address-line" style="top:292px"></div>
  <div class="address-line" style="top:329px"></div>

  <div class="call">
    <span class="call__label">Call now today!</span>
    <span class="call__phone">(555) 014-2387</span>
    <span class="call__address">P.O. Box 918, Maplecrest MI 48000</span>
  </div>
</section>

</body>
</html>
```